Conceptual Model Diagram for Replacing Medication with Behavior to Support Weight Loss Maintenance

Design a figure of a conceptual model that needs to be inserted into a word document for a QDV grant. This conceptual model illustrates how behavioral strategies can replace the regulatory functions lost after AOM discontinuation. The intervention targets three core vulnerabilities—appetite resurgence, metabolic inflexibility, and suboptimal mindstate—through the domains of Food, Physical Activity, and Mind. Sustained weight loss maintenance occurs at the intersection of these domains. The intervention is delivered within a design framework that makes behaviors easier to perform, aligns them with identity, and reinforces them through virtual support and community, ensuring real-world feasibility and long-term adherence.
Target Market(s)
QDV reviewers
Industry/Entity Type
academic
Font styles to use
Other font styles liked:
- arial
Requirements
Must have
- see my attached description

```html
<!DOCTYPE html>
<html lang="en">
<head>
<meta charset="utf-8">
<title>Conceptual Model: Behavior for Weight Loss Maintenance</title>
<link href="https://fonts.googleapis.com/css2?family=Arimo:ital,wght@0,400;0,700;1,400&display=swap" rel="stylesheet">
<style>
  :root {
    --mind: #fad8bd;
    --food: #c0bdd5;
    --activity: #b5e0f5;
    --mind-food: #bd9ea2;
    --mind-activity: #b3c6c5;
    --food-activity: #8aafdb;
    --core: #8a9db4;
    --orange: #e67e22;
    --navy: #231a63;
    --sky: #1a8fd6;
    --red: #d8262b;
    --ink: #1a1a1a;
    --highlight: #ffff00;
  }
  html, body {
    margin: 0;
    padding: 0;
    width: 1200px;
    height: 1200px;
    overflow: hidden;
    background: #fff;
  }
  .canvas {
    width: 1200px;
    height: 1200px;
    display: block;
    font-family: "Arimo", Arial, sans-serif;
  }
  .domain-label { font-weight: 700; fill: var(--ink); text-anchor: middle; }
  .outcome { font-weight: 700; text-anchor: middle; }
  .outcome--mind { fill: var(--orange); }
  .outcome--food { fill: var(--navy); }
  .outcome--activity { fill: var(--sky); }
  .core-label { font-weight: 700; fill: var(--highlight); text-anchor: middle; font-size: 21px; }
  .callout-title { font-weight: 700; fill: var(--red); text-anchor: middle; font-size: 30px; }
  .callout-body { fill: var(--ink); text-anchor: middle; font-size: 30px; }
  .note { fill: var(--red); font-style: italic; font-size: 26px; }
</style>
</head>
<body>
<svg class="canvas" viewBox="0 0 1932 1932" xmlns="http://www.w3.org/2000/svg">
  <defs>
    <clipPath id="clip-mind"><circle cx="965" cy="880" r="243"/></clipPath>
    <clipPath id="clip-food"><circle cx="811" cy="1160" r="243"/></clipPath>
    <clipPath id="clip-activity"><circle cx="1118" cy="1160" r="243"/></clipPath>
    <marker id="head-orange" markerWidth="6" markerHeight="6" refX="3" refY="3" orient="auto"><path d="M0,0 L6,3 L0,6 z" fill="var(--orange)"/></marker>
    <marker id="head-navy" markerWidth="6" markerHeight="6" refX="3" refY="3" orient="auto"><path d="M0,0 L6,3 L0,6 z" fill="var(--navy)"/></marker>
    <marker id="head-sky" markerWidth="6" markerHeight="6" refX="3" refY="3" orient="auto"><path d="M0,0 L6,3 L0,6 z" fill="var(--sky)"/></marker>
  </defs>

  <!-- dashed domain boundaries -->
  <g class="boundaries" fill="none" stroke-width="6" stroke-dasharray="12 9">
    <path d="M693,918 A275,275 0 1 1 1237,918" stroke="var(--orange)"/>
    <path d="M680,918 A275,275 0 1 0 960,1395" stroke="var(--navy)"/>
    <path d="M1250,918 A275,275 0 1 1 970,1395" stroke="var(--sky)"/>
  </g>

  <!-- domain circles -->
  <g class="domains">
    <circle cx="965" cy="880" r="243" fill="var(--mind)"/>
    <circle cx="811" cy="1160" r="243" fill="var(--food)"/>
    <circle cx="1118" cy="1160" r="243" fill="var(--activity)"/>
    <g clip-path="url(#clip-mind)"><circle cx="811" cy="1160" r="243" fill="var(--mind-food)"/></g>
    <g clip-path="url(#clip-mind)"><circle cx="1118" cy="1160" r="243" fill="var(--mind-activity)"/></g>
    <g clip-path="url(#clip-food)"><circle cx="1118" cy="1160" r="243" fill="var(--food-activity)"/></g>
    <g clip-path="url(#clip-mind)"><g clip-path="url(#clip-food)"><circle cx="1118" cy="1160" r="243" fill="var(--core)"/></g></g>
    <g fill="none" stroke="#fff" stroke-width="4">
      <circle cx="965" cy="880" r="243"/>
      <circle cx="811" cy="1160" r="243"/>
      <circle cx="1118" cy="1160" r="243"/>
    </g>
  </g>

  <!-- domain labels -->
  <text class="domain-label" x="965" y="785" font-size="50">MIND</text>
  <text class="domain-label" font-size="50" transform="translate(728,1245) rotate(45)">FOOD</text>
  <text class="domain-label" font-size="46" transform="translate(1198,1238) rotate(-45)">
    <tspan x="0" y="-10">PHYSICAL</tspan><tspan x="0" y="42">ACTIVITY</tspan>
  </text>

  <text class="core-label">
    <tspan x="965" y="1053">Sustained</tspan>
    <tspan x="965" y="1079">Weight Loss</tspan>
    <tspan x="965" y="1105">Maintenance</tspan>
  </text>

  <!-- vulnerability arrows -->
  <line x1="965" y1="692" x2="965" y2="462" stroke="var(--orange)" stroke-width="5" marker-end="url(#head-orange)"/>
  <line x1="700" y1="1280" x2="535" y2="1445" stroke="var(--navy)" stroke-width="4" marker-end="url(#head-navy)"/>
  <line x1="1245" y1="1297" x2="1410" y2="1462" stroke="var(--sky)" stroke-width="4" marker-end="url(#head-sky)"/>

  <text class="outcome outcome--mind" font-size="56">
    <tspan x="965" y="367">Suboptimal</tspan>
    <tspan x="965" y="428">Mindstate</tspan>
  </text>
  <text class="outcome outcome--food" font-size="50" transform="translate(468,1520) rotate(45)">
    <tspan x="0" y="-8">Appetite</tspan><tspan x="0" y="44">Resurgence</tspan>
  </text>
  <text class="outcome outcome--activity" font-size="50" transform="translate(1465,1515) rotate(-45)">
    <tspan x="0" y="-8">Metabolic</tspan><tspan x="0" y="44">Inflexibility</tspan>
  </text>

  <!-- design-framework callouts -->
  <g class="callout callout--mind">
    <rect x="322" y="457" width="387" height="155" rx="14" fill="#fff" stroke="var(--orange)" stroke-width="2.5"/>
    <polyline points="620,612 755,695 667,612" fill="#fff" stroke="var(--orange)" stroke-width="2.5"/>
    <line x1="622" y1="612" x2="665" y2="612" stroke="#fff" stroke-width="4"/>
    <text class="callout-title"><tspan x="516" y="495">VIRTUAL SUPPORT AND</tspan><tspan x="516" y="530">SOCIAL CONNECTION</tspan></text>
    <text class="callout-body"><tspan x="516" y="564">Accessibility, Community,</tspan><tspan x="516" y="598">Shared Accountability</tspan></text>
  </g>

  <g class="callout callout--food">
    <rect x="118" y="917" width="367" height="156" rx="14" fill="#fff" stroke="var(--navy)" stroke-width="2.5"/>
    <polyline points="400,1073 533,1157 447,1073" fill="#fff" stroke="var(--navy)" stroke-width="2.5"/>
    <line x1="402" y1="1073" x2="445" y2="1073" stroke="#fff" stroke-width="4"/>
    <text class="callout-title"><tspan x="301" y="962">MAKE IT EASY</tspan></text>
    <text class="callout-body"><tspan x="301" y="998">Habits, Routines,</tspan><tspan x="301" y="1032">Environment, Low friction</tspan></text>
  </g>

  <g class="callout callout--activity">
    <rect x="1447" y="917" width="368" height="156" rx="14" fill="#fff" stroke="var(--sky)" stroke-width="2.5"/>
    <polyline points="1487,1073 1398,1157 1533,1073" fill="#fff" stroke="var(--sky)" stroke-width="2.5"/>
    <line x1="1489" y1="1073" x2="1531" y2="1073" stroke="#fff" stroke-width="4"/>
    <text class="callout-title"><tspan x="1631" y="968">ALIGN WITH IDENTITY</tspan></text>
    <text class="callout-body"><tspan x="1631" y="1003">Self-concept, Maintain IT</tspan><tspan x="1631" y="1037">model, Internalization)</tspan></text>
  </g>

  <text class="note" x="96" y="1837">Diagram without title and caption</text>
</svg>
</body>
</html>
```